Postcard Design

www.lirvo.com.au
i am an occupational therapist and professionally trained coach. i work with children, parents and disability service providers to achieve brilliant outcomes for children with special needs.
http://www.lirvo.com.au/service/for-families
I need a postcard to give parents to promote our family service coaching service
A family service coach will work with you to set specific goals for your child, build a dream team, design and manage your child's highly effective therapy and educational team to ensure brilliant outcomes for your child..
KORLU - you have done my business card previously. they were great thank you.

```html
<!DOCTYPE html>
<html lang="en">
<head>
<meta charset="utf-8">
<title>Lirvo Family Service Coaching – Postcard</title>
<link rel="stylesheet" href="https://fonts.googleapis.com/css2?family=Montserrat:wght@300;500;700&family=Didact+Gothic&display=swap">
<style>
  :root{
    --teal:#3c9fb4;
    --navy:#344b64;
    --paper:#ffffff;
    --ground:#e9e6e1;
    --ink:#1d1d1d;
    --white:#ffffff;
    --soft-white:rgba(255,255,255,.85);
  }
  *{margin:0;padding:0;box-sizing:border-box}
  html,body{width:1200px;height:1000px;overflow:hidden;background:var(--ground)}
  .canvas{position:relative;width:1200px;height:1000px}

  .postcard{position:absolute;background:var(--paper);box-shadow:0 6px 18px rgba(0,0,0,.18);overflow:hidden}

  /* Back side */
  .postcard--back{left:30px;top:350px;width:820px;height:600px}
  .profile-band{position:absolute;left:22px;top:0;width:386px;height:150px;background:var(--teal)}
  .profile-photo{position:absolute;left:20px;top:26px;width:100px;height:100px;border-radius:50%;
    border:3px solid var(--white);background:radial-gradient(circle at 50% 40%,#c9a79a,#3a3d4a 75%)}
  .profile-name{position:absolute;left:140px;top:30px;font-family:'Didact Gothic',sans-serif;color:var(--white);line-height:1.35}
  .profile-name strong{display:block;font-family:'Montserrat',sans-serif;font-weight:700;font-size:14px}
  .profile-name span{display:block;font-size:14px;color:var(--soft-white)}
  .bio{position:absolute;left:22px;top:160px;width:384px;font-family:'Didact Gothic',sans-serif;
    font-size:12px;line-height:1.55;color:var(--ink);text-align:justify}
  .contact-panel{position:absolute;left:22px;top:478px;width:420px;height:122px;background:var(--navy);color:var(--white);
    font-family:'Didact Gothic',sans-serif}
  .contact-panel::before{content:"";position:absolute;left:300px;top:-10px;border:10px solid transparent;border-top:0;border-bottom-color:var(--navy)}
  .contact-brand{position:absolute;left:28px;top:16px;display:flex;align-items:center;gap:10px}
  .brand-dot{width:34px;height:34px;border-radius:50%;background:var(--white)}
  .brand-name{font-family:'Montserrat',sans-serif;font-weight:500;font-size:30px;color:var(--white);line-height:1}
  .contact-tag{position:absolute;left:112px;top:56px;font-size:10px;color:var(--soft-white)}
  .contact-role{position:absolute;left:28px;top:74px;font-size:13.5px}
  .contact-line{position:absolute;left:28px;top:96px;font-size:13.5px;font-family:'Montserrat',sans-serif;font-weight:700}
  .contact-line span{font-weight:300}
  .address-lines{position:absolute;left:450px;top:318px;width:330px}
  .address-lines i{display:block;height:2px;background:var(--ink);margin-bottom:42px}

  /* Front side */
  .postcard--front{left:440px;top:75px;width:740px;height:578px}
  .hero-photo{position:absolute;left:0;top:0;width:740px;height:355px;
    background:linear-gradient(100deg,#cfe3e6 0%,#e8dfd2 35%,#f1e6dc 55%,#d8b9a6 72%,#5d7ca8 100%)}
  .message{position:absolute;left:0;top:355px;width:470px;height:223px;background:var(--teal);padding:18px 24px 0 30px}
  .message::after{content:"";position:absolute;right:-18px;top:110px;border:9px solid transparent;border-left-color:var(--teal);border-right:0}
  .headline{font-family:'Montserrat',sans-serif;font-size:21px;line-height:1.4;color:var(--white);text-transform:uppercase;white-space:nowrap;font-weight:400}
  .headline .light{font-weight:300;color:rgba(255,255,255,.9)}
  .headline .bold{font-weight:700}
  .rule{height:1px;background:var(--white);margin:10px 0 9px;width:416px}
  .message p{font-family:'Didact Gothic',sans-serif;font-size:12px;line-height:1.6;color:var(--white);width:416px}
  .brand-panel{position:absolute;left:470px;top:355px;width:270px;height:223px;background:var(--navy)}
  .brand-panel .brand{position:absolute;left:46px;top:78px;display:flex;align-items:center;gap:12px}
  .brand-panel .brand-dot{width:44px;height:44px}
  .brand-panel .brand-name{font-size:36px}
  .brand-panel .brand-tag{position:absolute;left:102px;top:120px;font-family:'Didact Gothic',sans-serif;font-size:10.5px;color:var(--soft-white)}
</style>
</head>
<body>
<main class="canvas">

  <section class="postcard postcard--back" aria-label="Postcard back">
    <div class="profile-band">
      <div class="profile-photo" role="img" aria-label="Portrait photo of Mara Ellison"></div>
      <div class="profile-name">
        <strong>Mara Ellison</strong>
        <span>Occupational Therapist</span>
        <span>Coach</span>
        <span>Speaker</span>
      </div>
    </div>
    <p class="bio">Mara Ellison is the founder and director of Lirvo Consulting. She is an occupational therapist, business coach, disability service consultant, speaker and soon to be author. She works with individuals, families, allied health professionals and service providers to design great programmes that achieve brilliant outcomes for people with disabilities. Mara believes that every child is unique and has endless possibilities for growth, regardless of age, stage or diagnosis. Behind each child is a family and a team of service providers, they too need to bring their A game to the child's goal driven and individualised programme. Mara sits in the space between children, families and service providers, joyfully collaborating, coaching and consulting with all to ensure the best possible outcomes for children.</p>
    <div class="contact-panel">
      <div class="contact-brand"><span class="brand-dot"></span><span class="brand-name">lirvo</span></div>
      <div class="contact-tag">Family Service Coaching</div>
      <div class="contact-role">Occupational Therapist Coach, Speaker and Author</div>
      <div class="contact-line">mara@lirvo.com.au <span>|</span> Mobile 0412 555 207</div>
    </div>
    <div class="address-lines" aria-hidden="true"><i></i><i></i><i></i></div>
  </section>

  <section class="postcard postcard--front" aria-label="Postcard front">
    <div class="hero-photo" role="img" aria-label="Photo of a smiling family with a toddler and baby meeting a family service coach"></div>
    <div class="message">
      <h1 class="headline">
        <span class="light">Design and manage</span><br>
        <span class="light">your child's</span> <span class="bold">future with</span><br>
        <span class="bold">our highly effective therapy</span>
      </h1>
      <div class="rule"></div>
      <p>A family service coach will work with you to set specific goals for your child, build a dream team, design and manage your child's highly effective therapy and educational team to ensure brilliant outcomes for your child..</p>
    </div>
    <div class="brand-panel">
      <div class="brand"><span class="brand-dot"></span><span class="brand-name">lirvo</span></div>
      <div class="brand-tag">Family Service Coaching</div>
    </div>
  </section>

</main>
</body>
</html>
```